" A empresa é dividida em 2 segmentos, Informatica e automação comercial. Efetuamos de venda e prestação de serviços de informatica,redes,servidores para empresas em geral alem de manutenção de balanças, impressoras fiscais, leitores de códigos de barras para varejo em geral. "

```html
<!DOCTYPE html>
<html lang="pt-BR">
<head>
<meta charset="UTF-8">
<title>Vanta Automação Comercial — Cartão de visita</title>
<link href="https://fonts.googleapis.com/css2?family=Exo+2:wght@400;600;800&family=Roboto+Condensed:wght@400;700&display=swap" rel="stylesheet">
<style>
  :root {
    --page-bg: #e9e9ec;
    --card-white: #ffffff;
    --brand-blue: #1f4f9c;
    --brand-blue-deep: #173f82;
    --brand-blue-light: #6fb3ec;
    --ink-grey: #6d6f73;
    --line-light: rgba(140, 200, 250, 0.75);
    --text-on-blue: #ffffff;
  }
  * { box-sizing: border-box; margin: 0; padding: 0; }
  html, body {
    width: 1200px; height: 1200px; overflow: hidden;
    background: var(--page-bg);
    font-family: "Exo 2", sans-serif;
  }
  .sheet {
    width: 1200px; height: 1200px;
    display: flex; flex-direction: column; align-items: center; justify-content: center;
    gap: 60px;
  }
  .card {
    position: relative; width: 900px; height: 514px; overflow: hidden;
    box-shadow: 0 6px 18px rgba(0,0,0,0.12);
  }

  /* Front */
  .card--front { background: var(--card-white); }
  .brand-lockup {
    position: absolute; left: 0; right: 0; top: 130px;
    display: flex; flex-direction: column; align-items: center;
  }
  .brand-lockup__row { display: flex; align-items: center; gap: 26px; }
  .brand-lockup__square { width: 78px; height: 78px; background: var(--brand-blue); }
  .brand-lockup__name {
    font-weight: 800; font-size: 150px; line-height: 1; letter-spacing: 6px;
    color: var(--brand-blue);
  }
  .brand-lockup__tagline {
    margin-top: 14px;
    font-family: "Roboto Condensed", sans-serif; font-weight: 400;
    font-size: 34px; letter-spacing: 7px; text-transform: uppercase;
    color: var(--ink-grey);
  }
  .front-footer {
    position: absolute; left: 0; right: 0; bottom: 0; height: 56px;
    display: flex; align-items: center;
  }
  .front-footer__tab {
    width: 56px; height: 56px; background: var(--brand-blue);
    display: flex; align-items: center; justify-content: center;
  }
  .front-footer__url {
    margin-left: 24px;
    font-family: "Roboto Condensed", sans-serif; font-weight: 700;
    font-size: 26px; letter-spacing: 1px; color: var(--ink-grey);
  }

  /* Back */
  .card--back {
    background: linear-gradient(135deg, var(--brand-blue) 0%, var(--brand-blue-deep) 100%);
    color: var(--text-on-blue);
  }
  .back-decor {
    position: absolute; right: 0; top: 0; width: 480px; height: 230px;
    background: radial-gradient(ellipse at 80% 20%, rgba(111, 179, 236, 0.35) 0%, rgba(111, 179, 236, 0) 70%);
  }
  .back-name {
    position: absolute; left: 70px; top: 150px;
    font-weight: 600; font-size: 64px; line-height: 1; letter-spacing: 5px; color: var(--brand-blue-light);
  }
  .back-rule {
    position: absolute; left: 70px; right: 70px; top: 250px;
    height: 2px; background: var(--line-light);
  }
  .contact-list {
    position: absolute; left: 70px; right: 70px; top: 285px;
    list-style: none;
    font-family: "Roboto Condensed", sans-serif; font-size: 26px; line-height: 1;
  }
  .contact-list__item { display: flex; align-items: center; gap: 14px; margin-bottom: 16px; white-space: nowrap; }
  .contact-list__item--phones { gap: 60px; }
  .contact-list__phone { display: flex; align-items: center; gap: 14px; }
  .contact-icon { width: 22px; height: 22px; flex: none; }
</style>
</head>
<body>
<main class="sheet">

  <section class="card card--front" aria-label="Frente do cartão">
    <div class="brand-lockup">
      <div class="brand-lockup__row">
        <span class="brand-lockup__square"></span>
        <span class="brand-lockup__name">VANTA</span>
      </div>
      <span class="brand-lockup__tagline">Automação Comercial</span>
    </div>
    <footer class="front-footer">
      <div class="front-footer__tab">
        <svg width="26" height="26" viewBox="0 0 26 26" aria-hidden="true">
          <rect x="3" y="4" width="20" height="14" rx="1.5" fill="none" stroke="#fff" stroke-width="2.2"/>
          <rect x="9" y="20" width="8" height="2.4" fill="#fff"/>
        </svg>
      </div>
      <span class="front-footer__url">www.vantaautomacao.com.br</span>
    </footer>
  </section>

  <section class="card card--back" aria-label="Verso do cartão">
    <div class="back-decor" role="img" aria-label="Área decorativa com padrão geométrico em tons de azul claro"></div>

    <div class="back-name">VANTA</div>
    <div class="back-rule"></div>

    <ul class="contact-list">
      <li class="contact-list__item contact-list__item--phones">
        <span class="contact-list__phone">
          <svg class="contact-icon" viewBox="0 0 24 24" aria-hidden="true"><path fill="#fff" d="M6.6 10.8a15 15 0 0 0 6.6 6.6l2.2-2.2c.3-.3.7-.4 1-.2 1.1.4 2.3.6 3.6.6.6 0 1 .4 1 1V20c0 .6-.4 1-1 1A17 17 0 0 1 3 4c0-.6.4-1 1-1h3.5c.6 0 1 .4 1 1 0 1.3.2 2.5.6 3.6.1.3 0 .7-.2 1z"/></svg>
          (00) 0000-0000
        </span>
        <span class="contact-list__phone">
          <svg class="contact-icon" viewBox="0 0 24 24" aria-hidden="true"><rect x="6" y="2" width="12" height="20" rx="2" fill="none" stroke="#fff" stroke-width="2"/><circle cx="12" cy="18" r="1.3" fill="#fff"/></svg>
          (00) 0000-0000
        </span>
      </li>
      <li class="contact-list__item">
        <svg class="contact-icon" viewBox="0 0 24 24" aria-hidden="true"><rect x="2" y="5" width="20" height="14" rx="1.5" fill="none" stroke="#fff" stroke-width="2"/><path d="M3 6l9 7 9-7" fill="none" stroke="#fff" stroke-width="2"/></svg>
        contato@vantaautomacao.com.br
      </li>
      <li class="contact-list__item">
        <svg class="contact-icon" viewBox="0 0 24 24" aria-hidden="true"><circle cx="12" cy="12" r="8" fill="#fff"/></svg>
        facebook.com/vantaautomacao
      </li>
      <li class="contact-list__item">
        <svg class="contact-icon" viewBox="0 0 24 24" aria-hidden="true"><path fill="#fff" d="M12 2a7 7 0 0 0-7 7c0 5 7 13 7 13s7-8 7-13a7 7 0 0 0-7-7zm0 9.5A2.5 2.5 0 1 1 12 6.5a2.5 2.5 0 0 1 0 5z"/></svg>
        Rua xxxx xxxx, 00 - Bairro Xxxx Xxxxx · Cidade Xxxx - Estado
      </li>
    </ul>
  </section>

</main>
</body>
</html>
```